BrambleWorks business card

Looking for business card design that supports our company/software values. We have 2 logo designs at the moment but open to change if you think you can enhance the brand. Check out website www.brambleworks.com.au.

Target Market(s)

Education

Contact Information for Business Card

Name, title, mobile, email and website

Font styles to use
Sans Serif

Colors

Designer to choose colors to be used in the design.

Requirements
Must have
• BrambleWorks logo with tree and tagline on rear side with dark grey background colour

```html
<!DOCTYPE html>
<html lang="en">
<head>
<meta charset="utf-8">
<title>BrambleWorks business card</title>
<link href="https://fonts.googleapis.com/css2?family=Ubuntu:wght@400;500;700&display=swap" rel="stylesheet">
<style>
  :root {
    --page: #e6ebe4;
    --card: #f7f9f6;
    --card-edge: #d3dbd0;
    --green: #3f7a3a;
    --green-deep: #2c5a26;
    --ink: #1f2420;
    --text: #2a2f2b;
  }
  * { box-sizing: border-box; margin: 0; padding: 0; }
  html, body { width: 1200px; height: 800px; overflow: hidden; }
  body {
    background: var(--page);
    font-family: "Ubuntu", sans-serif;
    color: var(--text);
    position: relative;
  }
  .card {
    position: absolute;
    top: 250px;
    width: 520px;
    height: 300px;
    background: var(--card);
    border: 1px solid var(--card-edge);
    border-radius: 6px;
    overflow: hidden;
    box-shadow: 0 10px 30px rgba(40, 60, 40, 0.12);
  }
  .card--front { left: 60px; }
  .card--back { left: 620px; }

  .corner { position: absolute; }
  .corner--top-left { top: 0; left: 0; }
  .corner--bottom-right { bottom: 0; right: 0; }

  .brand {
    position: absolute;
    display: flex;
    align-items: center;
    gap: 10px;
    color: var(--ink);
    font-weight: 500;
    white-space: nowrap;
  }
  .brand__dot {
    border-radius: 50%;
    background: var(--green);
    flex: none;
  }
  .card--front .brand { left: 32px; top: 180px; font-size: 22px; }
  .card--front .brand__dot { width: 22px; height: 22px; }

  .divider {
    position: absolute;
    left: 256px;
    top: 60px;
    width: 2px;
    height: 196px;
    background: var(--green-deep);
  }
  .person {
    position: absolute;
    left: 282px;
    top: 40px;
  }
  .person__name {
    font-size: 25px;
    font-weight: 500;
    color: var(--green-deep);
    letter-spacing: 0.5px;
  }
  .person__name strong { color: var(--green); font-weight: 700; }
  .person__title {
    font-size: 14px;
    color: var(--ink);
    letter-spacing: 0.5px;
    margin-top: 2px;
  }
  .contacts {
    position: absolute;
    left: 282px;
    top: 126px;
    list-style: none;
    font-size: 13px;
    color: var(--ink);
  }
  .contacts li {
    display: flex;
    align-items: center;
    gap: 12px;
    height: 30px;
  }
  .contacts svg { width: 18px; height: 18px; flex: none; }
  .contacts .address { line-height: 1.2; font-size: 12.5px; }

  .card--back .brand {
    left: 110px;
    top: 80px;
    font-size: 40px;
  }
  .card--back .brand__dot { width: 36px; height: 36px; }
  .tagline-rule {
    position: absolute;
    left: 164px;
    top: 138px;
    width: 262px;
    height: 2px;
    background: var(--green-deep);
  }
  .tagline {
    position: absolute;
    left: 172px;
    top: 148px;
    font-size: 18px;
    color: var(--ink);
    letter-spacing: 0.3px;
    white-space: nowrap;
  }
  .back-web {
    position: absolute;
    left: 0;
    right: 0;
    bottom: 30px;
    text-align: center;
    font-size: 14px;
    color: var(--ink);
  }
</style>
</head>
<body>

<section class="card card--front" aria-label="Card front">
  <svg class="corner corner--top-left" width="170" height="150" viewBox="0 0 170 150">
    <polygon points="0,0 170,0 0,150" fill="var(--green)"/>
    <polygon points="0,150 170,0 128,0 0,118" fill="var(--ink)"/>
    <polygon points="0,118 128,0 0,0" fill="var(--green-deep)" opacity="0.55"/>
  </svg>

  <div class="brand"><span class="brand__dot"></span>BrambleWorks</div>

  <div class="divider"></div>

  <div class="person">
    <p class="person__name">NAME <strong>HERE</strong></p>
    <p class="person__title">DESIGNATION</p>
  </div>

  <ul class="contacts">
    <li>
      <svg viewBox="0 0 24 24"><path fill="var(--green-deep)" d="M6.6 10.8a15 15 0 0 0 6.6 6.6l2.2-2.2a1 1 0 0 1 1-.25 11.4 11.4 0 0 0 3.6.6 1 1 0 0 1 1 1V20a1 1 0 0 1-1 1A17 17 0 0 1 3 4a1 1 0 0 1 1-1h3.5a1 1 0 0 1 1 1c0 1.25.2 2.45.6 3.6a1 1 0 0 1-.25 1z"/></svg>
      0123 456 789
    </li>
    <li>
      <svg viewBox="0 0 24 24"><rect x="2.5" y="5" width="19" height="14" fill="none" stroke="var(--green-deep)" stroke-width="1.6"/><polyline points="2.5,5 12,13 21.5,5" fill="none" stroke="var(--green-deep)" stroke-width="1.6"/></svg>
      hello@brambleworks.com
    </li>
    <li>
      <svg viewBox="0 0 24 24"><circle cx="12" cy="12" r="9" fill="none" stroke="var(--green-deep)" stroke-width="1.6"/><ellipse cx="12" cy="12" rx="4" ry="9" fill="none" stroke="var(--green-deep)" stroke-width="1.4"/><line x1="3" y1="12" x2="21" y2="12" stroke="var(--green-deep)" stroke-width="1.4"/></svg>
      www.brambleworks.com
    </li>
    <li>
      <svg viewBox="0 0 24 24"><path fill="var(--green-deep)" d="M12 2a7 7 0 0 0-7 7c0 5.2 7 13 7 13s7-7.8 7-13a7 7 0 0 0-7-7zm0 9.5A2.5 2.5 0 1 1 12 6.5a2.5 2.5 0 0 1 0 5z"/></svg>
      <span class="address">Address Line 1 Here,<br>Address Line 2 Here</span>
    </li>
  </ul>
</section>

<section class="card card--back" aria-label="Card back">
  <div class="brand"><span class="brand__dot"></span>BrambleWorks</div>
  <div class="tagline-rule"></div>
  <p class="tagline">Student Success Platform</p>
  <p class="back-web">www.brambleworks.com</p>

  <svg class="corner corner--bottom-right" width="190" height="110" viewBox="0 0 190 110">
    <polygon points="190,0 190,110 0,110" fill="var(--green)"/>
    <polygon points="190,0 190,28 40,110 0,110" fill="var(--ink)"/>
    <polygon points="190,28 190,110 40,110" fill="var(--green-deep)"/>
  </svg>
</section>

</body>
</html>
```